We need a poster designed for use on facebook, as well as to print out for advertising in local noticeboards and shop windows.
The poster will advertise the Tallowbrook Turf Club 30th Anniversary Ball.
the ball will be held on the 28th April 2018 at the Tallowbrook Community Hall.
Time will be 630pm till late. Ticket Price is $120 which includes 3 course dinner, drinks on arrival and entertainment during the evening.
Additional details will need to be added to the poster at a later date.
The tallowbrook Turf Club is a horse racing club run by the community. The club has been incorporateds for 30 years. This Ball will be a celebration of that anniversary.

Target Market(s)

Middlemount Community

Industry/Entity Type

Club

Font styles to use
Serif
Decorative

Colors
1b1b1b
fbfbfb
6b449b
886aae
a64599
ffc214

Requirements
Must have
• Include
• where when time and cost
• ticket inclusions
• entertainement by Colin Verity
Nice to have
• Attached are some images for inspiration.
• It would be nice to have the race club logo included somewhere however not prominant.
Should not have
• Abstract geometriic lines
• images of people
• primary colours

```html
<!DOCTYPE html>
<html lang="en">
<head>
<meta charset="utf-8">
<title>Tallowbrook Turf Club 30th Anniversary Ball</title>
<link href="https://fonts.googleapis.com/css2?family=Great+Vibes&family=Montserrat:ital,wght@0,500;1,500&display=swap" rel="stylesheet">
<style>
  :root {
    --page: #eef1f6;
    --navy: #17123f;
    --gold: #f6bb22;
    --gold-soft: rgba(246, 187, 34, 0.28);
    --white: #fbfbfb;
    --ink: #1b1b1b;
  }
  * { margin: 0; padding: 0; box-sizing: border-box; }
  html, body { width: 1200px; height: 1200px; overflow: hidden; background: var(--page); }
  .poster {
    position: absolute; left: 200px; top: 40px; width: 800px; height: 1120px;
    background: var(--navy); color: var(--gold);
    font-family: "Montserrat", sans-serif; font-weight: 500;
    box-shadow: 0 14px 34px rgba(0,0,0,0.25);
  }
  .frame-outer, .frame-inner { position: absolute; border: 3px solid var(--gold); }
  .frame-outer { inset: 20px; }
  .frame-inner { inset: 30px; border-width: 2px; }
  .corner-ornament {
    position: absolute; width: 78px; height: 78px;
    background: radial-gradient(circle, var(--gold-soft), transparent 70%);
  }
  .corner-ornament.tl { left: 40px; top: 40px; }
  .corner-ornament.tr { right: 40px; top: 40px; }
  .corner-ornament.bl { left: 40px; bottom: 40px; }
  .corner-ornament.br { right: 40px; bottom: 40px; }
  .star {
    position: absolute; width: 64px; height: 64px;
    background: radial-gradient(circle, rgba(246,187,34,0.45), transparent 65%);
  }
  .club-tab {
    position: absolute; left: 336px; top: 20px; width: 128px; height: 170px;
    background: var(--white); border: 3px solid var(--gold); border-top: none;
    clip-path: polygon(0 0, 100% 0, 100% 100%, 50% 82%, 0 100%);
    display: flex; flex-direction: column; align-items: center; justify-content: center;
    gap: 8px; padding: 0 10px 30px; text-align: center;
  }
  .club-tab .dot { width: 34px; height: 34px; border-radius: 50%; background: var(--navy); }
  .club-tab .club-name {
    font-size: 12px; line-height: 1.3; color: var(--navy); font-variant: small-caps; letter-spacing: 0.5px;
  }
  .flourish {
    position: absolute; left: 40px; top: 320px; width: 720px; height: 290px;
    background: radial-gradient(ellipse at center, rgba(246,187,34,0.10), transparent 70%);
  }
  .caps { position: absolute; left: 0; width: 100%; text-align: center; font-variant: small-caps; letter-spacing: 1px; }
  .club-heading { top: 222px; font-size: 30px; }
  .script { position: absolute; font-family: "Great Vibes", cursive; color: var(--gold); line-height: 1; white-space: nowrap; }
  .script.years { left: 470px; top: 318px; font-size: 46px; }
  .script.anniversary { left: 0; width: 100%; text-align: center; top: 360px; font-size: 132px; }
  .script.ball { left: 0; width: 100%; text-align: center; top: 478px; font-size: 120px; padding-left: 40px; }
  .date { top: 672px; font-size: 26px; }
  .date sup { font-size: 13px; }
  .venue { top: 744px; font-size: 22px; }
  .time { top: 806px; font-size: 22px; }
  .tickets { top: 866px; font-size: 24px; }
  .inclusions { position: absolute; left: 0; width: 100%; top: 900px; text-align: center; font-style: italic; font-size: 17px; line-height: 24px; }
  .entertainment { top: 980px; font-size: 20px; }
</style>
</head>
<body>
  <main class="poster">
    <div class="frame-outer"></div>
    <div class="frame-inner"></div>

    <div class="corner-ornament tl" role="img" aria-label="Gold filigree corner ornament"></div>
    <div class="corner-ornament tr" role="img" aria-label="Gold filigree corner ornament"></div>
    <div class="corner-ornament bl" role="img" aria-label="Gold filigree corner ornament"></div>
    <div class="corner-ornament br" role="img" aria-label="Gold filigree corner ornament"></div>

    <div class="star" style="left:150px; top:140px" role="img" aria-label="Gold starburst"></div>
    <div class="star" style="left:640px; top:270px" role="img" aria-label="Gold starburst"></div>
    <div class="star" style="left:90px; top:790px" role="img" aria-label="Gold starburst"></div>
    <div class="star" style="left:630px; top:790px" role="img" aria-label="Gold starburst"></div>

    <div class="club-tab">
      <span class="dot"></span>
      <span class="club-name">Tallowbrook Turf Club</span>
    </div>

    <div class="flourish" role="img" aria-label="Gold calligraphic flourishes around the title"></div>

    <p class="caps club-heading">Tallowbrook Turf Club</p>
    <h1>
      <span class="script years">30th</span>
      <span class="script anniversary">Anniversary</span>
      <span class="script ball">Ball</span>
    </h1>

    <p class="caps date">28<sup>th</sup> April, 2018</p>
    <p class="caps venue">At the Tallowbrook Community Hall</p>
    <p class="caps time">Time: 6:30 pm till late</p>
    <p class="caps tickets">Tickets : $120</p>
    <p class="inclusions">(inclusive of 3 course dinner, drinks on arrival<br>and entertainment during the evening)</p>
    <p class="caps entertainment">Entertainment by Colin Verity</p>
  </main>
</body>
</html>
```